Business Stationery - New Business card design

We are looking for some new business stationery, including business cards (double sided), compliment slips & letterheads for our offices in the UK, Ireland, North Carolina (US) & our Holdings company.

We are open to all ideas; however we are ideally looking for something that does not look corporate.

Our website is www.talvonahumancapital.example – this is the style of branding that we are currently using.

Here is some of the information that should be included;

Business Cards

Front
Logo
Name – Desmond Varrow
Job Title - Director
Direct line number - +353 (0)1 468 2071
Office number - +353 (0)1 482 6150
Email address – d.varrow@talvonahc.example
Website address – www.talvonahumancapital.example

Back
Logo
‘Specialists in IT Recruitment’
LinkedIn – Talvona Human Capital
Twitter - @talvonahire
An image included – possibly ‘Image 1’ attached?

Letterheads & Compliment slips

UK (A4 size)
Logo
Phone numbers for the various offices;
London: +44 (0)20 7961 3327
Belfast: +44 (0)28 9037 6615
Dublin: +353 (0)1 482 6150
Raleigh, NC: +1 919 642 1357
Address: 2nd Floor, 118 Marlowe Street, London W1C 4PJ
Email: info@talvonahc.example
Website: www.talvonahumancapital.example
Social media icons for LinkedIn & Twitter
Talvona Human Capital Registered in England & Wales No. 6815337 VAT No. 871342609

Ireland (A4 size)
Logo
Address: 4-7 Corran Street, Dublin 2 D02 KX58, Ireland
Email: info@talvonahc.example
Talvona Human Capital (Ireland) Registered in Ireland No. 624903 VAT No. 7182635KK

USA (letter size)

Logo
Address: 542 N. Pellam Street, Raleigh, North Carolina 27605, United States
Email: info@talvonahc.example
Talvona Human Capital Inc. Registered in the State of North Carolina No. 2640917

Holdings (A4 size)

Logo
Address: 58 Fenwick Street, Belfast BT27JD
Email: info@talvonahc.example
Talvona Human Capital (Holdings) Ltd Registered in Northern Ireland No. NI583076

Target Market(s)

IT Professionals

Industry/Entity Type

It Professional

Contact Information for Business Card

Front
Logo
Name – Desmond Varrow
Job Title - Director

Back
Logo
Twitter - @talvonahire

```html
<!DOCTYPE html>
<html lang="en">
<head>
<meta charset="utf-8">
<title>Talvona Human Capital – Stationery</title>
<link href="https://fonts.googleapis.com/css2?family=Lato:wght@300;400;700;900&family=Roboto+Condensed:wght@300;400&family=Raleway:wght@400;700&display=swap" rel="stylesheet">
<style>
  :root{
    --bg:#d9e3ee;
    --paper:#ffffff;
    --brand-blue:#1a5aa8;
    --card-blue:#0f5aa6;
    --brand-green:#5aab3c;
    --ink:#5a5a5a;
    --ink-dark:#4d4d4d;
    --shadow:0 3px 8px rgba(40,60,90,.25);
  }
  *{margin:0;padding:0;box-sizing:border-box}
  html,body{width:1200px;height:893px;overflow:hidden}
  body{background:var(--bg);position:relative;font-family:"Lato",sans-serif;color:var(--ink)}
  .sheet{position:absolute;background:var(--paper);box-shadow:var(--shadow)}
  .abs{position:absolute}

  /* wordmark */
  .wordmark{position:absolute;color:var(--brand-blue);font-family:"Lato",sans-serif;font-weight:400;line-height:1}
  .wordmark .name{display:block;letter-spacing:.02em}
  .wordmark .sub{display:block}

  .ico{width:7px;height:7px;fill:var(--brand-green);display:inline-block;vertical-align:middle}

  /* letterhead */
  .letterhead{left:102px;top:119px;width:462px;height:653px}
  .letterhead .wordmark{left:44px;top:44px}
  .letterhead .wordmark .name{font-size:35px}
  .letterhead .wordmark .sub{font-size:12px;letter-spacing:.42em;margin:6px 0 0 13px}
  .lh-contact{right:44px;top:26px;text-align:right;font-size:6.9px;line-height:9px;color:var(--ink)}
  .lh-contact .addr{margin-bottom:3px}
  .lh-contact .row{display:flex;justify-content:flex-end;align-items:center;gap:5px}
  .lh-date{left:44px;top:172px;font-size:10.5px;font-weight:300;color:var(--ink)}
  .lh-recipient{left:44px;top:191px;font-size:16px;font-weight:900;color:var(--ink-dark);letter-spacing:.01em}
  .lh-role{left:44px;top:214px;font-size:10.5px;font-weight:300}
  .lh-body{left:44px;top:256px;width:374px;font-family:"Roboto Condensed",sans-serif;font-weight:300;font-size:8.7px;line-height:16.1px;color:var(--ink-dark);text-align:justify}
  .lh-body p{margin-bottom:16px}
  .lh-signoff{left:44px;top:501px;font-family:"Roboto Condensed",sans-serif;font-weight:300;font-size:10.5px;color:var(--ink-dark)}
  .lh-signature{left:44px;top:527px;width:48px;height:34px;background:linear-gradient(135deg,#e6edf6,#d3deec);border-radius:3px}
  .lh-footer{left:0;right:0;top:599px;text-align:center;line-height:12px}
  .lh-footer .company{color:var(--brand-blue);font-weight:700;font-size:11px;margin-bottom:1px}
  .lh-footer .reg{color:var(--brand-green);font-size:9px}

  /* business card front */
  .card-front{left:659px;top:160px;width:196px;height:111px}
  .card-front .wordmark{left:14px;top:44px}
  .card-front .wordmark .name{font-size:14.5px}
  .card-front .wordmark .sub{font-size:4.6px;letter-spacing:.42em;margin:2px 0 0 5px}
  .card-divider{left:98px;top:32px;width:1px;height:44px;background:var(--brand-blue)}
  .card-name{left:108px;top:31px;font-size:8.5px;font-weight:700;color:var(--brand-blue)}
  .card-title{left:108px;top:42px;font-size:4.6px;color:var(--ink)}
  .card-contact{left:108px;top:52px;font-size:4.6px;line-height:6.4px;color:var(--ink)}
  .card-contact .row{display:flex;align-items:center;gap:4px}
  .card-contact .ico{width:4.5px;height:4.5px}

  /* business card back */
  .card-back{left:661px;top:310px;width:196px;height:111px;background:var(--card-blue)}
  .card-art{left:55px;top:13px;width:86px;height:65px;border-radius:6px;background:radial-gradient(ellipse at 50% 55%,#f3f6fa 0%,#d8e6f3 45%,rgba(15,90,166,0) 75%)}
  .card-tagline{left:0;right:0;top:83px;text-align:center;font-size:4.6px;color:var(--brand-green);font-weight:700}
  .card-band{left:0;right:0;top:95px;height:8px;background:var(--brand-green);display:flex;justify-content:center;align-items:center;gap:8px;font-size:4.6px;color:#fff}
  .card-band .item{display:flex;align-items:center;gap:3px}
  .card-band .sq{width:4.5px;height:4.5px;background:#fff;border-radius:.8px}

  /* compliment slip */
  .comp-slip{left:621px;top:534px;width:484px;height:218px}
  .comp-slip .wordmark{left:30px;top:30px}
  .comp-slip .wordmark .name{font-size:35px}
  .comp-slip .wordmark .sub{font-size:12px;letter-spacing:.42em;margin:6px 0 0 13px}
  .cs-heading{right:23px;top:43px;font-size:9.6px;font-weight:700;color:var(--brand-blue);letter-spacing:.01em}
  .cs-address{left:22px;top:150px;font-size:6.7px;line-height:8px}
  .cs-col{top:170px;font-size:6.7px;line-height:9px}
  .cs-col .row{display:flex;align-items:center;gap:5px}
  .cs-col-phones{left:22px}
  .cs-col-web{left:147px}
  .cs-legal{right:23px;top:179px;text-align:right;font-size:6.7px;line-height:9px}
  .cs-legal .company{color:var(--brand-blue);font-weight:700}
</style>
</head>
<body>
<svg width="0" height="0" style="position:absolute" aria-hidden="true">
  <defs>
    <symbol id="i-phone" viewBox="0 0 10 10"><path d="M1 3.2C1 2 2 1.3 5 1.3S9 2 9 3.2v.8H7V3H3v1H1zM2.2 8.8l.9-3.6h3.8l.9 3.6zM5 5.8a1 1 0 1 0 0 2 1 1 0 0 0 0-2z"/></symbol>
    <symbol id="i-mobile" viewBox="0 0 10 10"><path d="M3 .5h4a.6.6 0 0 1 .6.6v7.8a.6.6 0 0 1-.6.6H3a.6.6 0 0 1-.6-.6V1.1A.6.6 0 0 1 3 .5zm.4 1v6.4h3.2V1.5z"/></symbol>
    <symbol id="i-mail" viewBox="0 0 10 10"><path d="M.5 2h9v6h-9zm1 1v.3L5 5.6l3.5-2.3V3zm0 1.5V7h7V4.5L5 6.8z"/></symbol>
    <symbol id="i-globe" viewBox="0 0 10 10"><path d="M5 .6a4.4 4.4 0 1 1 0 8.8A4.4 4.4 0 0 1 5 .6zm0 1a3.4 3.4 0 1 0 0 6.8A3.4 3.4 0 0 0 5 1.6z"/><circle cx="5" cy="5" r="2.2"/></symbol>
    <symbol id="i-square" viewBox="0 0 10 10"><rect x=".8" y=".8" width="8.4" height="8.4" rx="1.5"/></symbol>
  </defs>
</svg>

<!-- Letterhead -->
<section class="sheet letterhead">
  <div class="wordmark"><span class="name">TALVONA</span><span class="sub">Human Capital</span></div>

  <div class="abs lh-contact">
    <div class="addr">2nd Floor, 118 Marlowe Street,<br>London W1C 4PJ</div>
    <div class="row">London: +44 (0)20 7961 3327 <svg class="ico"><use href="#i-phone"/></svg></div>
    <div class="row">Belfast: +44 (0)28 9037 6615 <svg class="ico"><use href="#i-phone"/></svg></div>
    <div class="row">Dublin: +353 (0)1 482 6150 <svg class="ico"><use href="#i-phone"/></svg></div>
    <div class="row">Raleigh, NC: +1 919 642 1357 <svg class="ico"><use href="#i-phone"/></svg></div>
    <div class="row">info@talvonahc.example <svg class="ico"><use href="#i-mail"/></svg></div>
    <div class="row">www.talvonahumancapital.example <svg class="ico"><use href="#i-globe"/></svg></div>
    <div class="row">Talvona Human Capital <svg class="ico"><use href="#i-square"/></svg></div>
    <div class="row">@talvonahire <svg class="ico"><use href="#i-square"/></svg></div>
  </div>

  <div class="abs lh-date">10 December, 2020</div>
  <div class="abs lh-recipient">MARTIN HALE</div>
  <div class="abs lh-role">Cheif Executive Officer</div>

  <div class="abs lh-body">
    <p>Contrary to popular belief, Lorem Ipsum is not simply random text. It has roots in a piece of classical Latin literature from 45 BC, making it over 2000 years old. Harold Penwick, a Latin professor at Ashbourne-Leigh College in Virginia, looked up one of the more obscure Latin words, consectetur.</p>
    <p>Lorem Ipsum comes from sections 1.10.32 and 1.10.33 of "de Finibus Bonorum et Malorum" (The Extremes of Good and Evil) by Orlan, written in 45 BC. This book is a treatise on the theory of ethics, very popular during the Renaissance. The first line of Lorem Ipsum.</p>
    <p>The standard chunk of Lorem Ipsum used since the 1500s is reproduced below for those interested. Sections 1.10.32 and 1.10.33 from "de Finibus Bonorum et Malorum" by Orlan are also reproduced in their exact original.</p>
    <p>The standard chunk of Lorem Ipsum used since the 1500s is reproduced below for those interested.</p>
  </div>

  <div class="abs lh-signoff">Best Regards</div>
  <div class="abs lh-signature" role="img" aria-label="Handwritten signature"></div>

  <div class="abs lh-footer">
    <div class="company">Talvona Human Capital</div>
    <div class="reg">Registered in England &amp; Wales No. 6815337</div>
    <div class="reg">VAT No. 871342609</div>
  </div>
</section>

<!-- Business card front -->
<section class="sheet card-front">
  <div class="wordmark"><span class="name">TALVONA</span><span class="sub">Human Capital</span></div>
  <div class="abs card-divider"></div>
  <div class="abs card-name">Desmond Varrow</div>
  <div class="abs card-title">Director</div>
  <div class="abs card-contact">
    <div class="row"><svg class="ico"><use href="#i-phone"/></svg>+353 (0)1 482 6150</div>
    <div class="row"><svg class="ico"><use href="#i-mobile"/></svg>+353 (0)1 468 2071</div>
    <div class="row"><svg class="ico"><use href="#i-mail"/></svg>d.varrow@talvonahc.example</div>
    <div class="row"><svg class="ico"><use href="#i-globe"/></svg>www.talvonahumancapital.example</div>
  </div>
</section>

<!-- Business card back -->
<section class="sheet card-back">
  <div class="abs card-art" role="img" aria-label="Isometric city illustration with office towers, clouds and planes"></div>
  <div class="abs card-tagline">‘Specialists in IT Recruitment’</div>
  <div class="abs card-band">
    <span class="item"><span class="sq"></span>Talvona Human Capital</span>
    <span class="item"><span class="sq"></span>@talvonahire</span>
  </div>
</section>

<!-- Compliment slip -->
<section class="sheet comp-slip">
  <div class="wordmark"><span class="name">TALVONA</span><span class="sub">Human Capital</span></div>
  <div class="abs cs-heading">WITH COMPLIMENTS</div>

  <div class="abs cs-address">2nd Floor, 118 Marlowe Street,<br>London W1C 4PJ</div>

  <div class="abs cs-col cs-col-phones">
    <div class="row"><svg class="ico"><use href="#i-phone"/></svg>London: +44 (0)20 7961 3327</div>
    <div class="row"><svg class="ico"><use href="#i-phone"/></svg>Belfast: +44 (0)28 9037 6615</div>
    <div class="row"><svg class="ico"><use href="#i-phone"/></svg>Dublin: +353 (0)1 482 6150</div>
    <div class="row"><svg class="ico"><use href="#i-phone"/></svg>Raleigh, NC: +1 919 642 1357</div>
  </div>

  <div class="abs cs-col cs-col-web">
    <div class="row"><svg class="ico"><use href="#i-mail"/></svg>info@talvonahc.example</div>
    <div class="row"><svg class="ico"><use href="#i-globe"/></svg>www.talvonahumancapital.example</div>
    <div class="row"><svg class="ico"><use href="#i-square"/></svg>Talvona Human Capital</div>
    <div class="row"><svg class="ico"><use href="#i-square"/></svg>@talvonahire</div>
  </div>

  <div class="abs cs-legal">
    <div class="company">Talvona Human Capital</div>
    <div>Registered in England &amp; Wales No. 6815337</div>
    <div>VAT No. 871342609</div>
  </div>
</section>
</body>
</html>
```